Flyer für ambulanten Pflegedienst
Zielgruppe
Ambulanter Pflegedienst in Gründung. Habe schon ein Logo und Text. Zielgruppe sind Pflege und Hilfsbedürftige Menschen

```html
<!DOCTYPE html>
<html lang="de">
<head>
<meta charset="utf-8">
<title>Pflegeweg – Flyer</title>
<link rel="stylesheet" href="https://fonts.googleapis.com/css2?family=Poppins:wght@400;600;700&family=Playfair+Display:ital,wght@0,700;1,400&display=swap">
<style>
  :root{
    --teal:#4fbdb5;
    --teal-dark:#2fa9a6;
    --blue:#1896c6;
    --blue-deep:#1286b8;
    --ink:#1d1d1d;
    --bg:#b9b9b9;
    --paper:#ffffff;
  }
  *{box-sizing:border-box;margin:0;padding:0}
  html,body{width:1200px;height:1117px;overflow:hidden}
  body{background:var(--bg);font-family:"Poppins",sans-serif;color:var(--ink);position:relative}
  .page{position:absolute;top:182px;width:530px;height:752px;background:var(--paper);overflow:hidden}
  .page--front{left:57px}
  .page--back{left:613px}
  .abs{position:absolute}
  .wave{position:absolute;left:0;width:530px}
  .body-text{font-size:8.6px;line-height:1.25}
  .centered{text-align:center}
  ul.list{list-style:none;font-size:8.6px;line-height:1.32}
  ul.list li{position:relative;padding-left:10px}
  ul.list li::before{content:"•";position:absolute;left:0;color:var(--ink)}
  ul.list--teal li::before{color:var(--teal)}
  .brand{left:152px;top:44px;width:320px}
  .brand__name{font-family:"Poppins",sans-serif;font-weight:700;font-size:24px;color:var(--blue);line-height:1}
  .brand__mark{position:absolute;left:-44px;top:-16px;width:36px;height:36px;border-radius:50%;background:var(--teal)}
  .brand__sub{font-family:"Poppins",sans-serif;font-size:7px;color:var(--teal-dark);margin-top:4px;font-weight:600}
  .brand__legal{font-family:"Poppins",sans-serif;font-size:6.5px;color:var(--teal-dark);letter-spacing:1px;margin-top:2px;padding-left:36px}
  .highlight{color:var(--blue);font-weight:700}
  .pill{position:absolute;height:17px;border-radius:9px;background:var(--teal);color:#fff;font-weight:600;font-size:10.5px;text-align:center;line-height:17px}
  .heading{font-weight:700;font-size:10.5px;color:var(--teal);line-height:1.2}
  .heading--blue{color:var(--blue)}
  .photo-ring{position:absolute;left:272px;top:508px;width:208px;height:208px;border-radius:50%;border:7px solid var(--teal)}
  .photo{position:absolute;left:282px;top:518px;width:188px;height:188px;border-radius:50%;background:radial-gradient(circle at 45% 45%,#f1ddd0 0%,#d9b8a3 45%,#c9c4bf 100%)}
  .divider{position:absolute;left:70px;top:368px;width:405px;height:1.5px;background:var(--teal)}
  .claim{position:absolute;left:0;width:530px;top:655px;text-align:center;font-family:"Playfair Display",serif;font-style:italic;font-size:21px;color:var(--teal)}
  .contact{position:absolute;color:#fff;font-weight:600;font-size:9.2px;display:flex;align-items:center;gap:5px}
  .contact svg{width:10px;height:10px}
  .contact-sep{position:absolute;left:192px;top:704px;width:1px;height:30px;background:#fff}
  .cols{display:flex;gap:10px}
</style>
</head>
<body>

<!-- Vorderseite -->
<section class="page page--front">
  <svg class="wave" style="top:0" height="110" viewBox="0 0 530 110" preserveAspectRatio="none">
    <path d="M0 0H530V10C380 20 200 14 0 48Z" fill="var(--teal)"/>
    <path d="M0 48C70 30 130 22 190 18C110 36 45 66 0 108Z" fill="var(--blue)"/>
  </svg>

  <div class="abs brand">
    <span class="brand__mark"></span>
    <div class="brand__name">Pflegeweg</div>
    <div class="brand__sub">ambulanter Pflegedienst Hallenberg UG</div>
    <div class="brand__legal">Haftungsbeschränkt</div>
  </div>

  <p class="abs body-text centered" style="left:52px;top:113px;width:426px">Uns liegt es am Herzen durch qualitativ hochwertige und individuelle Unterstützungsleistungen den Menschen ein selbstbestimmtes Leben zu ermöglichen. Wir setzen auf Fachkompetenz und Empathie, um sicherzustellen, dass unsere Kunden die bestmögliche medizinische Versorgung erhalten.</p>
  <p class="abs body-text centered" style="left:52px;top:170px;width:426px">Unsere Dienstleistung umfasst die ambulante Pflege gemäß SGB XI sowie die Behandlungspflege gemäß SGB V. Betreuungs- und Entlastungszeiten nach § 45 SGB XI um Menschen im Alltag zu unterstützen und ihre Lebensqualität zu steigern.</p>
  <p class="abs body-text centered" style="left:52px;top:218px;width:426px">Pflegebedürftig ist, wer aufgrund einer körperlichen, geistigen oder seelischen Krankheit bzw. Behinderung in erheblichen Umfang Hilfe bis hin zur vollumfänglichen Betreuung benötigt. Die Leistungen des Altenpflege- erstrecken sich auf die<br><span class="highlight">Grundpflege, Behandlungspflege, 24-Stundenpflege,<br>ambulante Palliativ Pflege, hauswirtschaftliche Versorgung,<br>Verhinderungspflege und Alltagsbegleitung.</span></p>

  <div class="pill" style="left:54px;top:303px;width:184px">Grundpflege</div>
  <p class="abs body-text" style="left:54px;top:327px;width:184px">Zu pflegende Personen werden bei den alltäglichen Grundverrichtungen unterstützt z.B.</p>
  <ul class="abs list" style="left:54px;top:369px">
    <li>Duschen</li><li>Baden</li><li>Zahnpflege Kämmen</li><li>Rasieren</li><li>An- und Auskleiden</li><li>Hilfsmittelversorgung</li><li>Mobilisation</li><li>Prophylaxen</li><li>Nahrungsaufnahme</li><li>Toilettengang u.s.w.</li>
  </ul>

  <div class="pill" style="left:268px;top:303px;width:212px">Behandlungspflege</div>
  <p class="abs body-text" style="left:268px;top:327px;width:212px">Die Behandlungspflege umfasst alle Pflegedienste, die auf ärztlicher Verordnung hin vom Pflegepersonal durchgeführt werden, z. B.</p>
  <ul class="abs list" style="left:268px;top:381px;width:210px">
    <li>Pulsmessung</li><li>Blutdruckmessung</li><li>Blutzuckermessung</li><li>Wundversorgung</li><li>Verbandswechsel</li><li>Injektionen (z.b. Insulin)</li><li>Stellen der Medikamente</li><li>Anlegen von Kompressionsverbänden</li><li>An- und Ausziehen von Kompressionsstrümpfen u.s.w.</li>
  </ul>

  <div class="pill" style="left:54px;top:504px;width:184px">24-Stunden Pflege</div>
  <p class="abs body-text" style="left:54px;top:529px;width:190px">In verschiedenen Situationen ist die stundenweise Pflege nicht ausreichend, z.B. in der Folgezeit eines Krankenhausaufenthaltes. Es wird eine 24-Stunden-Pflege angeboten, im Rahmen derer das Pflegepersonal rund um die Uhr erreichbar ist. Typische Leistungen sind:</p>
  <ul class="abs list" style="left:54px;top:634px;width:190px">
    <li>Überwachung der Vitalsituation des Patienten</li><li>Verabreichung von Medikamenten</li><li>Wundversorgung</li><li>Verbandswechsel</li><li>Katheter Versorgung u.s.w.</li>
  </ul>

  <div class="photo-ring"></div>
  <div class="photo" role="img" aria-label="Foto: Pflegekraft mit einer älteren Dame, beide lächelnd"></div>

  <svg class="wave" style="top:682px" height="70" viewBox="0 0 530 70" preserveAspectRatio="none">
    <path d="M0 10C150 40 340 50 530 14" fill="none" stroke="var(--teal)" stroke-width="2"/>
    <path d="M0 22C150 50 350 58 530 24V70H0Z" fill="var(--blue)"/>
  </svg>
</section>

<!-- Rückseite -->
<section class="page page--back">
  <svg class="wave" style="top:0" height="110" viewBox="0 0 530 110" preserveAspectRatio="none">
    <path d="M0 0H530V10C380 20 200 14 0 48Z" fill="var(--teal)"/>
    <path d="M0 48C70 30 130 22 190 18C110 36 45 66 0 108Z" fill="var(--blue)"/>
  </svg>

  <h2 class="abs heading" style="left:110px;top:36px">Hauswirtschaftliche<br>Versorgung</h2>
  <p class="abs body-text" style="left:56px;top:65px;width:190px">In der hauswirtschaftlichen Versorgung werden sämtliche hauswirtschaftlichen Tätigkeiten übernommen, z.B.</p>
  <ul class="abs list list--teal" style="left:56px;top:103px;width:200px">
    <li>Einkaufen</li><li>Besorgungen</li><li>Zubereitung von Mahlzeiten</li><li>AbwaschenWäsche waschen</li><li>Bügeln</li><li>Reinigungsarbeiten (Aufräumen, Toilette, Bad, Küche, Wohn- und Schlafbereich, Staubsaugen, Staubwischen)</li><li>Betreuung von Haustieren</li><li>Heizen der Wohnung (Holz, Kohle, Öl)</li><li>Fahrdienste</li>
  </ul>

  <h2 class="abs heading" style="left:272px;top:34px">Betreuungs- und<br>Entlastungsleistungen nach §<br>45 SGB XI</h2>
  <p class="abs body-text" style="left:272px;top:75px;width:205px">Voraussetzung ist das Vorliegen eines Pflegegrades. Bei der Antragstellung eines Pflegegrades sind wir behilflich und begleiten die Begutachtung durch den Medizinischen Dienst der Krankenkassen.</p>
  <ul class="abs list list--teal" style="left:272px;top:132px;width:205px">
    <li>Unterstützung bei der Haushaltsführung</li><li>Einkaufen</li><li>Begleitung zu Ärzten</li><li>Arzttermine vereinbaren</li><li>Unterstützung beim Ausfüllen von Formularen und Anträgen</li><li>Spaziergänge</li>
  </ul>

  <h2 class="abs heading" style="left:272px;top:229px">Alltagsbegleitung</h2>
  <p class="abs body-text" style="left:272px;top:246px;width:210px">In der Alltagsbegleitung werden die Pflegepersonen in allen alltäglichen Tätigkeiten und Freizeitaktivitäten unterstützt und begleitet. Typische Leistungen sind z.B.</p>
  <div class="abs cols" style="left:272px;top:292px">
    <ul class="list list--teal" style="width:94px">
      <li>Arztbesuche</li><li>Behördengänge</li><li>Kulturelle Veranstaltungen</li><li>Spaziergänge</li><li>Ausflüge</li>
    </ul>
    <ul class="list list--teal" style="width:100px">
      <li>Wanderungen</li><li>Stadtbummel</li><li>Restaurantbesuche</li><li>Friseurbesuche</li><li>Gedächtnistraining u.s.w.</li>
    </ul>
  </div>

  <h2 class="abs heading" style="left:56px;top:249px">Verhinderungspflege</h2>
  <p class="abs body-text" style="left:56px;top:265px;width:192px">Das Angebot im Bereich Verhinderungspflege richtet sich an die Angehörigen, die bei der Pflege eine stundenweise Entlastung benötigen. Typische Anlässe sind z.B.</p>
  <ul class="abs list list--teal" style="left:56px;top:319px;display:flex;gap:14px">
    <li>Urlaub</li><li>Krankheit</li><li>Überlastung</li>
  </ul>

  <div class="divider"></div>

  <p class="abs body-text" style="left:54px;top:380px;width:430px">Der Altenpflege- führt sämtliche Pflegeleistungen kompetent, professionell und zuverlässig aus. Das oberste Ziel der Pflege ist die Sicherung und Verbesserung der Lebensqualität und das Bewahren des gewohnten Lebensumfelds der Pflegepersonen. Krankenhaus- und Betreuungsheimaufenthalte sollen möglichst vermieden werden. Diesem Grundgedanken liegt die Erkenntnis zu Grunde, dass in einer vertrauten Umgebung Kranke oft schneller gesünder werden und gerade ältere Menschen sich zu. Hause besonders wohl und geborgen fühlen.</p>
  <p class="abs body-text" style="left:54px;top:455px;width:430px">Der grundlegende Geschäftsprozess des Unternehmens gliedert sich in die Bereiche Beratung, Pflegekonzept, Vertragsabschluss und Pflege:</p>

  <h2 class="abs heading heading--blue" style="left:54px;top:484px">Beratung</h2>
  <p class="abs body-text" style="left:54px;top:500px;width:180px">Kunden werden ausführlich unter Berücksichtigung ihrer Wünsche und Vorstellungen beraten. Denn das vorhandene Pflegeangebot bietet eine Vielzahl an Möglichkeiten. Wichtig ist der Aufbau von Vertrauen.</p>

  <h2 class="abs heading heading--blue" style="left:54px;top:576px">Pflegekonzept</h2>
  <p class="abs body-text" style="left:54px;top:592px;width:190px">Unter Berücksichtigung aller Möglichkeiten und Patientenwünsche wird ein individuelles Leistungskonzept entwickelt und eine verbindliche Kostenaufstellung erstellt.</p>

  <h2 class="abs heading heading--blue" style="left:269px;top:484px">Vertragsschluss</h2>
  <p class="abs body-text" style="left:269px;top:500px;width:210px">Alle Aufträge mit Kunden werden in schriftlicher Form geschlossen und beidseitig unterzeichnet.</p>

  <h2 class="abs heading heading--blue" style="left:269px;top:545px">Pflege</h2>
  <p class="abs body-text" style="left:269px;top:561px;width:215px">Die vereinbarten Pflegeleistungen werden nun umgesetzt. Dabei kann der Kunde stets eine hohe Ausführungsqualität erwarten. Es wird für jeden Kunden eine Mappe zur Pflegedokumentation geführt (Pflegesoftware, die stets vom Kunden sowie seinen Angehörigen eingesehen werden kann).</p>

  <svg class="wave" style="top:642px" height="110" viewBox="0 0 530 110" preserveAspectRatio="none">
    <path d="M0 28C130 50 300 66 530 38V110H0Z" fill="var(--blue)"/>
    <path d="M260 64C380 58 470 40 530 16V40C450 58 370 64 260 64Z" fill="var(--teal)"/>
  </svg>

  <div class="claim">Wir sind für Sie da</div>

  <div class="contact" style="left:54px;top:706px">
    <svg viewBox="0 0 10 10"><circle cx="5" cy="5" r="5" fill="#fff"/><path d="M3 2.5l1 1-0.6 0.8c0.4 0.9 1 1.5 1.9 1.9l0.8-0.6 1 1-0.8 1C4.3 7.4 2.6 5.7 2.5 3.3Z" fill="var(--blue)"/></svg>
    Telefon: 000-111-2233
  </div>
  <div class="contact" style="left:54px;top:723px">
    <svg viewBox="0 0 10 10"><circle cx="5" cy="5" r="5" fill="#fff"/><rect x="2.5" y="4" width="5" height="3" fill="var(--blue)"/><rect x="3.5" y="2.5" width="3" height="1.5" fill="var(--blue)"/></svg>
    Fax: 000-111-2233
  </div>
  <div class="contact-sep"></div>
  <div class="contact" style="left:205px;top:706px">
    <svg viewBox="0 0 10 10"><circle cx="5" cy="5" r="5" fill="#fff"/><rect x="2.5" y="3.2" width="5" height="3.6" fill="none" stroke="var(--blue)" stroke-width="0.8"/><path d="M2.5 3.2L5 5.2 7.5 3.2" fill="none" stroke="var(--blue)" stroke-width="0.8"/></svg>
    Email: info@pflegeweg.example
  </div>
  <div class="contact" style="left:205px;top:723px">
    <svg viewBox="0 0 10 10"><path d="M5 0.5C3 0.5 1.6 2 1.6 3.8 1.6 6.3 5 9.5 5 9.5S8.4 6.3 8.4 3.8C8.4 2 7 0.5 5 0.5Z" fill="#fff"/><circle cx="5" cy="3.8" r="1.3" fill="var(--blue)"/></svg>
    Anschrift: 01234 Musterfeld, Lindenweg 7
  </div>
</section>

</body>
</html>
```